Real Estate Office Front Facade Redesign - ideas needed

Kindly read this brief thoroughly as there are 2 deliverables:
1. Office building façade redesign (see attached logo and also photo of our office building façade)
2. I also require a design for a freestanding signboard that will be coordinated with the design of the office front please see the images attached labelled signboard.

Deliverable number 1:
I am looking for a minimalist contemporary design with strong colours to draw the attention of the passing Traffic.

The office facade is to be repainted so you may choose to recolour the office in any way to coordinate with logo however the attached logo must remain as is. I prefer the colours red black and white or shades of these colours.

Vireo property managers is a new company looking to target property investors in the local area. Most of our clients are from a middle to upper income demographic. We help these investors to rent out their properties and ensure they are maintained in good condition and provide a regular income.

The area we operate in is centrally located and close to the central business district of Perth.

Our office is situated in a residential area on a busy road facing diagonally at 45° down the road. People see our office from their cars whilst driving to work, there is no pedestrian traffic in the area. Therefore the office façade needs to stand out and any signage must be read by quickly passing traffic or convey our brand in seconds. Whilst the view of the office from the road is obscured somewhat by trees from a distance, once within 50 to 100 m of the office the full face of the office front is visible facing directly at the driver.

No measurements are provided for the façade of the office (please see the photo provided), this is a blank canvas as the whole building will be repainted to fit in with YOUR design. A logo is also attached. The colours red black and white are preferred.

Please provide an image of the office with signage/colours superimposed.

Deliverable number 2:
Also attached is an image of a freestanding sign for which I require a design. This sign is used for advertising properties for lease or sale which will be erected outside the front of residential houses. Again this sign needs to be bold and bright with a contemporary design. It needs to stand out from the crowd of many other signs in the area, whilst the sign advertises the property it must also promote our company brand by having a prominent logo. The size of these signboards will either be 1250 mm x 900 mm or 1800 mm x 625 mm. Please note that this sign must be rectangular in shape and cannot have any text or logo protruding outside of the lines of the rectangular sign due to cost restrictions.

Target Market(s)

Industry/Entity Type

Real Estate

Font styles to use
Sans Serif

Colors
ec1f27
ffffff
000000

Requirements
Must have
• Contemporary uncluttered design using the colours red black and white of shades of.
Nice to have
• A prominent logo with the words "Property Managers" easily read by passing traffic.
• Files provided with editable text and the name of the font used.
Should not have
• designs protruding outside of the overall building facia or sign rectangle.

```html
<!DOCTYPE html>
<html lang="en">
<head>
<meta charset="utf-8">
<title>Vireo Property Managers – For Lease Signboard</title>
<link rel="stylesheet" href="https://fonts.googleapis.com/css2?family=Raleway:wght@300;400;500&display=swap">
<style>
  :root {
    --slate: #3b4046;
    --slate-deep: #2b2f34;
    --red: #ec1f27;
    --white: #ffffff;
    --soft-white: #e9eaeb;
  }
  * { margin: 0; padding: 0; box-sizing: border-box; }
  html, body {
    width: 900px;
    height: 1200px;
    overflow: hidden;
    background: var(--slate);
  }
  .signboard {
    position: relative;
    width: 900px;
    height: 1200px;
    background: var(--slate);
    font-family: "Raleway", sans-serif;
    color: var(--white);
  }
  .brand {
    position: absolute;
    top: 200px;
    left: 0;
    width: 100%;
    text-align: center;
  }
  .brand-row {
    display: flex;
    align-items: center;
    justify-content: center;
    gap: 28px;
  }
  .brand-dot {
    width: 64px;
    height: 64px;
    border-radius: 50%;
    background: var(--red);
    flex: none;
  }
  .brand-name {
    font-size: 120px;
    font-weight: 400;
    letter-spacing: 2px;
    line-height: 1;
  }
  .brand-tagline {
    margin-top: 26px;
    font-size: 38px;
    font-weight: 400;
    letter-spacing: 2px;
    line-height: 1;
    color: var(--soft-white);
  }
  .listing-type {
    position: absolute;
    top: 520px;
    width: 100%;
    text-align: center;
    font-weight: 300;
    line-height: 1;
  }
  .listing-type .for {
    display: block;
    font-size: 132px;
    letter-spacing: 4px;
  }
  .listing-type .lease {
    display: block;
    margin-top: 30px;
    font-size: 180px;
    letter-spacing: 6px;
  }
  .contact-band {
    position: absolute;
    top: 890px;
    left: 0;
    width: 100%;
    height: 205px;
    background: var(--slate-deep);
  }
  .contact-line {
    position: absolute;
    white-space: nowrap;
    line-height: 1;
  }
  .contact-line .label {
    font-size: 48px;
    font-weight: 400;
    color: var(--soft-white);
  }
  .contact-line .number {
    font-size: 66px;
    font-weight: 500;
    margin-left: 14px;
  }
  .contact-mobile { top: 50px; left: 144px; }
  .contact-office { top: 130px; left: 216px; }
  .web-bar {
    position: absolute;
    bottom: 0;
    left: 0;
    width: 100%;
    height: 105px;
    background: var(--red);
    text-align: center;
    font-size: 48px;
    font-weight: 400;
    line-height: 105px;
    letter-spacing: 1px;
  }
</style>
</head>
<body>
  <main class="signboard">
    <header class="brand">
      <div class="brand-row">
        <span class="brand-dot" aria-hidden="true"></span>
        <h1 class="brand-name">Vireo</h1>
      </div>
      <p class="brand-tagline">Property Managers</p>
    </header>

    <h2 class="listing-type">
      <span class="for">FOR</span>
      <span class="lease">LEASE</span>
    </h2>

    <section class="contact-band">
      <p class="contact-line contact-mobile">
        <span class="label">Mobile :</span><span class="number">0400 123 456</span>
      </p>
      <p class="contact-line contact-office">
        <span class="label">Office :</span><span class="number">9400 1234</span>
      </p>
    </section>

    <footer class="web-bar">www.vireoproperty.com.au</footer>
  </main>
</body>
</html>
```